Plakat-Design für ein großes, geistliches Konzert für Chor, Orchester und Solisten
Zielgruppe
Wir sind eine Kantorei einer Kirchengemeinde, die in jedem Jahr ein großes Konzert für Chor, Orchester und Solisten veranstaltet. In diesem Jahr ist das Konzert in doppeltem Sinn etwas Besonderes. Zum einen weil wir das Konzert in Kooperation mit einer anderen Kantorei bestreiten und zum anderen weil die Anzahl der Mitwirkenden so groß ist, dass wir nicht der Kirche sondern das Konzert in die hiesige Stadthalle verlagern. Die Kirchenmusik präsentiert sozusagen sich außerhalb ihrer eigenen Mauern.
Eine Zielgruppe sollen diejenigen sein, die sich durch den besoneren Veranstaltungsort ansprechen lassen, also eher kirchenfremde Menschen. Das Plakat sollte auch das bestehende Stammpublikum nicht abschrecken, sondern einladen.
Es ist ein Folgeauftrag geplant, und zwar ein Programmheft/Textheft für das Konzert mit dem gleichen Design als Grundlage.
Aufgabenstellung
Das Plakat soll im DIN A3 oder A4 Hochformat erstellt werden.
Zwei weitere Logos von Förderern folgen noch.
Außer der Turm sind alle Logos von Förderern.
Der Turm ist sozusagen unser Markenzeichen und ein Wiedererkennungsmerkmal.
Das Konzert steht unter dem Motto: Von der Finsternis zum Licht.
Bezüglich der Textgröße sollte dieses Motto nicht größer sein als z.B. der Komponist und das Werk. Vielmehr soll das Motto durch ein grafisches Element eingearbeitet werden. 'Brautigorff' und 'Sternruf' sollen Eye catcher-Worte sein. Sternruf ist der Titel des Konzertes!

```html
<!DOCTYPE html>
<html lang="de">
<head>
<meta charset="utf-8">
<title>Von der Finsternis zum Licht – Konzertplakat</title>
<link href="https://fonts.googleapis.com/css2?family=Oswald:wght@300;400;500;600&family=Space+Mono&display=swap" rel="stylesheet">
<style>
  :root {
    --backdrop: #8a8889;
    --magenta: #b0147e;
    --ink: #231f20;
    --paper: #ffffff;
    --soft-grey: #c8c3c7;
    --info-pink: #c2198c;
    --blush: #f2dcec;
  }
  * { margin: 0; padding: 0; box-sizing: border-box; }
  html, body { width: 1200px; height: 1200px; overflow: hidden; background: var(--backdrop); }
  .poster {
    position: absolute; left: 216px; top: 58px; width: 768px; height: 1086px;
    background: var(--ink); overflow: hidden;
  }
  .header-band { position: absolute; left: 0; top: 0; width: 768px; height: 241px; background: var(--magenta); }
  .programme {
    position: absolute; left: 24px; top: 22px;
    font-family: "Oswald", sans-serif; font-weight: 400; font-size: 29px; line-height: 30px;
    color: var(--soft-grey); text-transform: uppercase; letter-spacing: 0.2px;
    transform: scaleX(0.82); transform-origin: left top;
  }
  .programme strong { color: var(--paper); font-weight: 600; }
  .hero-photo {
    position: absolute; left: 0; top: 241px; width: 768px; height: 724px;
    background:
      radial-gradient(ellipse 240px 200px at 520px 430px, rgba(255,214,230,0.85), rgba(230,150,180,0.45) 45%, rgba(0,0,0,0) 100%),
      radial-gradient(ellipse 300px 260px at 500px 520px, rgba(196,110,120,0.6), rgba(0,0,0,0) 100%),
      linear-gradient(100deg, rgba(0,0,0,0) 52%, rgba(215,210,225,0.55) 66%, rgba(0,0,0,0) 80%),
      linear-gradient(180deg, #1a1416 0%, #2b1f24 60%, #3a2028 100%);
  }
  .motto {
    position: absolute; right: 25px;
    font-family: "Space Mono", monospace; font-size: 87px; line-height: 1; text-align: right;
    white-space: nowrap;
  }
  .motto-dark { color: var(--ink); }
  .motto-light { color: var(--paper); }
  .motto-1 { top: 84px; }
  .motto-2 { top: 155px; }
  .motto-3 { top: 231px; }
  .credits {
    position: absolute; left: 27px; top: 348px; width: 200px;
    font-family: "Oswald", sans-serif; font-weight: 400; font-size: 11px; line-height: 13px;
    text-transform: uppercase; letter-spacing: 0.6px;
  }
  .credits p { margin-bottom: 13px; }
  .credits .label { color: var(--paper); }
  .credits .value { color: var(--info-pink); }
  .event-date {
    position: absolute; right: 25px; top: 870px;
    font-family: "Oswald", sans-serif; font-weight: 500; font-size: 42px; line-height: 40px;
    text-transform: uppercase; text-align: right; color: var(--soft-grey);
    transform: scaleX(0.78); transform-origin: right top; white-space: nowrap;
  }
  .event-date b { color: var(--paper); font-weight: 500; }
  .sponsor-strip {
    position: absolute; left: 0; top: 965px; width: 768px; height: 121px; background: var(--paper);
  }
  .sponsor-strip svg { position: absolute; left: 0; top: 0; }
  .sponsor {
    position: absolute; font-family: "Oswald", sans-serif; white-space: nowrap;
  }
  .sponsor-church { left: 242px; top: 60px; font-size: 15px; font-weight: 400; color: var(--magenta); }
  .sponsor-foundation { left: 428px; top: 54px; font-size: 21px; font-weight: 400; color: var(--ink); text-transform: uppercase; letter-spacing: 1px; }
  .sponsor-friends { left: 629px; top: 42px; font-size: 16px; line-height: 22px; font-weight: 500; color: var(--ink); text-transform: uppercase; }
</style>
</head>
<body>
  <main class="poster">
    <div class="header-band"></div>
    <div class="hero-photo" role="img" aria-label="Foto: geöffnete, nach oben gewandte Hände in einem hellen Lichtstrahl vor dunklem Hintergrund"></div>

    <div class="programme">
      Felix Brautigorff-<strong>Lindquist</strong>: Choralkantate<br>
      „Wer nur den lieben Gott lässt walten“<br>
      <strong>Sternruf</strong>-Sinfonie op. 52
    </div>

    <div class="motto motto-dark motto-1">Von der</div>
    <div class="motto motto-dark motto-2">Finsternis</div>
    <div class="motto motto-light motto-3">zum Licht</div>

    <section class="credits">
      <p><span class="label">Sopran</span><br><span class="value">Olivia Brandt und<br>Julia-Sophie Keller</span><br><span class="label">Tenor</span><br><span class="value">Martin Ekholm</span></p>
      <p><span class="value">Kammersymphonie Marbrunn<br>Kirchenkreiskantorei Ellerstedt<br>Kantorei St. Petri, Hollbrück</span></p>
      <p><span class="label">Gesamtleitung</span><br><span class="value">Kirchenkreiskantoren<br>Markus Hellwein (ELL)<br>und Raphael Strunk (HB)</span></p>
      <p><span class="label">Einlass</span> <span class="value">17.30 Uhr</span></p>
      <p><span class="label">Eintrittspreise</span><br><span class="value">25,- / 20,- / 15,- Euro<br>(Ermässigungen 50%)</span></p>
      <p><span class="label">Kartenvorverkauf</span><br><span class="value">Kulturverein Hollbrück,<br>Mühlweg 7, 12345 HB</span></p>
      <p><span class="label">Weitere Informationen unter</span><br><span class="value">www.petri-hollbrueck.de<br>www.kulturverein-hollbrueck.de<br>www.stadthalle-hollbrueck.de</span></p>
    </section>

    <div class="event-date">
      Sonntag, <b>22.09.2019</b> um <b>18.00</b><br>
      <b>Uhr</b> in der Stadthalle Hollbrück
    </div>

    <footer class="sponsor-strip">
      <svg width="768" height="121" viewBox="0 0 768 121" aria-hidden="true">
        <defs>
          <linearGradient id="blushFade" x1="0" y1="0" x2="0" y2="1">
            <stop offset="0" stop-color="#f6e6f1"/>
            <stop offset="1" stop-color="#ecd2e4"/>
          </linearGradient>
        </defs>
        <path d="M0 0 H230 C250 40 270 100 300 121 H0 Z" fill="url(#blushFade)"/>
      </svg>
      <div class="sponsor sponsor-church">Kirchenkreis Hollbrück</div>
      <div class="sponsor sponsor-foundation">Hollbrück Stiftung</div>
      <div class="sponsor sponsor-friends">Freundeskreis<br>Kirchenmusik</div>
    </footer>
  </main>
</body>
</html>
```